Brevanta Interiors
Business Card, Stationery Package, Email Signature
Project: Brevanta Interiors
Brevanta Interiors -
Creative Brief
Professional
Marisol Pryde
Managing Director
P.O.Box 4372 Larkmoor, TX 70000 - 4372
mpryde@brevantainteriors.example
www.brevantainteriors.example
Brevanta Interiors is a retail store offering Flooring products and Installation services. We would like to have the following items made: Business Card, Stationery Package (Fax, Letterhead, Envelopes, etc.), and Email Signature. We would like to see two types of fonts created for comparison, the original font and one of your own professional choices. Winner, please provide all design templates for future modification upon completion of the contest. Thank you!
logo, text, slogan, and web address.

```html
<!DOCTYPE html>
<html lang="en">
<head>
<meta charset="utf-8">
<title>Brevanta Interiors – Stationery</title>
<link href="https://fonts.googleapis.com/css2?family=Open+Sans:wght@400;600;700&display=swap" rel="stylesheet">
<style>
  :root {
    --backdrop: #6b4a33;
    --paper: #ffffff;
    --navy: #1d2f8a;
    --blue: #3c5bc4;
    --green: #2f8f4e;
    --ink: #2a2f45;
    --muted: #7a8094;
    --tag: #e7d8c8;
    --faint: rgba(90, 167, 154, 0.16);
    --fold: #d9dde6;
  }
  * { box-sizing: border-box; margin: 0; padding: 0; }
  html, body { width: 1200px; height: 307px; overflow: hidden; }
  body {
    position: relative;
    background: var(--backdrop);
    font-family: "Open Sans", Arial, sans-serif;
    color: var(--ink);
  }
  .item { position: absolute; background: var(--paper); box-shadow: 0 2px 5px rgba(0,0,0,.35); overflow: hidden; }
  .brand { display: flex; align-items: center; gap: 4px; font-weight: 700; color: var(--navy); white-space: nowrap; }
  .brand .dot { width: 6px; height: 6px; background: var(--green); border-radius: 50%; flex: none; }

  /* stand-alone logo */
  .logo-lockup { position: absolute; left: 12px; top: 40px; width: 160px; background: none; box-shadow: none; }
  .logo-lockup .brand { font-size: 13px; color: #fff; }
  .logo-lockup .brand .dot { width: 10px; height: 10px; }
  .logo-lockup .tag { font-size: 7px; color: var(--tag); margin: 4px 0 0 14px; }

  /* business cards */
  .card-front { left: 12px; top: 113px; width: 108px; height: 67px; padding: 5px 6px; }
  .card-front::before { content: ""; position: absolute; left: 0; right: 0; top: 0; height: 19px; background: linear-gradient(90deg, var(--blue), var(--navy)); }
  .card-front .brand { position: relative; font-size: 6px; color: #fff; margin-top: 1px; }
  .card-front .details { position: absolute; left: 6px; top: 25px; right: 4px; font-size: 4px; line-height: 1.5; color: var(--muted); white-space: nowrap; }
  .card-front .details strong { color: var(--ink); font-size: 5px; }
  .card-back { top: 211px; width: 58px; height: 46px; display: flex; align-items: center; justify-content: center; }
  .card-back .brand { font-size: 4.5px; gap: 3px; }
  .card-back .brand .dot { width: 5px; height: 5px; }
  .card-back.one { left: 19px; }
  .card-back.two { left: 84px; }

  /* letterheads */
  .letterhead { top: 12px; width: 196px; height: 271px; }
  .letterhead.first { left: 276px; }
  .letterhead.second { left: 497px; }
  .letterhead .band { height: 22px; background: linear-gradient(90deg, #fff 15%, var(--blue) 60%, var(--navy)); display: flex; align-items: center; padding: 0 8px; }
  .letterhead .brand { font-size: 6px; }
  .letterhead .contact { position: absolute; right: 8px; top: 5px; font-size: 3.5px; color: #fff; text-align: right; line-height: 1.4; }
  .letterhead .mark { position: absolute; left: 50%; top: 50%; transform: translate(-50%, -50%); width: 70px; height: 70px; border-radius: 50%; background: var(--faint); }
  .letterhead .foot { position: absolute; bottom: 8px; left: 0; right: 0; text-align: center; font-size: 3.5px; color: var(--muted); }

  /* small envelopes */
  .env-small { left: 700px; width: 152px; }
  .env-small.top { top: 74px; height: 95px; }
  .env-small.bottom { top: 180px; height: 90px; }
  .env-small .band { height: 14px; background: linear-gradient(90deg, #fff 20%, var(--blue) 70%, var(--navy)); display: flex; align-items: center; padding: 0 6px; }
  .env-small .brand { font-size: 5px; }
  .env-small .addr { position: absolute; left: 6px; top: 18px; font-size: 3px; color: var(--muted); }

  /* long envelopes */
  .env-long { left: 871px; width: 305px; height: 84px; }
  .env-long svg { position: absolute; inset: 0; }
  .env-long.green { top: 12px; }
  .env-long.blue { top: 108px; }
  .env-long.plain { top: 204px; }
  .env-long .brand { position: absolute; left: 50%; top: 48px; transform: translateX(-50%); font-size: 5px; }
</style>
</head>
<body>

  <div class="item logo-lockup">
    <div class="brand"><span class="dot"></span>Brevanta Interiors</div>
    <div class="tag">Flooring &amp; Installation</div>
  </div>

  <div class="item card-front">
    <div class="brand"><span class="dot"></span>Brevanta Interiors</div>
    <div class="details">
      <strong>Marisol Pryde</strong><br>
      Managing Director<br>
      P.O.Box 4372 Larkmoor, TX 70000 - 4372<br>
      mpryde@brevantainteriors.example<br>
      www.brevantainteriors.example
    </div>
  </div>
  <div class="item card-back one"><div class="brand"><span class="dot"></span>Brevanta Interiors</div></div>
  <div class="item card-back two"><div class="brand"><span class="dot"></span>Brevanta Interiors</div></div>

  <div class="item letterhead first">
    <div class="band"><div class="brand"><span class="dot"></span>Brevanta Interiors</div></div>
    <div class="contact">mpryde@brevantainteriors.example<br>www.brevantainteriors.example</div>
    <div class="mark" role="img" aria-label="Faint brand watermark"></div>
    <div class="foot">P.O.Box 4372 Larkmoor, TX 70000 - 4372</div>
  </div>
  <div class="item letterhead second">
    <div class="band"><div class="brand"><span class="dot"></span>Brevanta Interiors</div></div>
    <div class="contact">mpryde@brevantainteriors.example<br>www.brevantainteriors.example</div>
    <div class="mark" role="img" aria-label="Faint brand watermark"></div>
    <div class="foot">P.O.Box 4372 Larkmoor, TX 70000 - 4372</div>
  </div>

  <div class="item env-small top">
    <div class="band"><div class="brand"><span class="dot"></span>Brevanta Interiors</div></div>
    <div class="addr">P.O.Box 4372 Larkmoor, TX 70000 - 4372</div>
  </div>
  <div class="item env-small bottom">
    <div class="band"><div class="brand"><span class="dot"></span>Brevanta Interiors</div></div>
    <div class="addr">P.O.Box 4372 Larkmoor, TX 70000 - 4372</div>
  </div>

  <div class="item env-long green">
    <svg viewBox="0 0 305 84" width="305" height="84"><polygon points="0,0 305,0 152,44" fill="var(--green)"/><polyline points="0,84 152,40 305,84" fill="none" stroke="var(--fold)" stroke-width="1"/></svg>
  </div>
  <div class="item env-long blue">
    <svg viewBox="0 0 305 84" width="305" height="84"><polygon points="0,0 305,0 152,44" fill="var(--navy)"/><polyline points="0,84 152,40 305,84" fill="none" stroke="var(--fold)" stroke-width="1"/></svg>
  </div>
  <div class="item env-long plain">
    <svg viewBox="0 0 305 84" width="305" height="84"><polyline points="0,0 152,40 305,0" fill="none" stroke="var(--fold)" stroke-width="1"/></svg>
    <div class="brand"><span class="dot"></span>Brevanta Interiors</div>
  </div>

</body>
</html>
```